New Stationary for our business

We are a gift business and would like to create a new corporate image with new stationary and design.

We would like a Classic Corporate look with a touch of Flair.

We would need:
Envelopes
Letter Head
Business Cards
With Comp Slips
Note Pads
Etc...

Our details are:

Basket Haven Pty Ltd
518 Pelling Street, Carrow Vale, Victoria, 3071
1800 742 918
www.baskethaven.com.au
sales@baskethaven.com.au

ABN: 62 804 319 775

Target Market(s)

Corporate Look

Industry/Entity Type

Marketing

Contact Information for Business Card

Basket Haven Pty Ltd
1800 742 918
518 Pelling Street
Carrow Vale 3071
Victoria Australia

Darren Pelloni - Managing Director
darren.pelloni@baskethaven.com.au
0417 586 902

Logo Text

Basket Haven - The Present Experts

Colors

Designer to choose colors to be used in the design.

Requirements
Must have
• Look and Feel upmarket and exclusive

```html
<!DOCTYPE html>
<html lang="en">
<head>
<meta charset="utf-8">
<title>Basket Haven – Business Card</title>
<link href="https://fonts.googleapis.com/css2?family=Roboto:wght@400;500;700&display=swap" rel="stylesheet">
<style>
  :root {
    --backdrop: #d9d6d1;
    --card-stock: #ebe9e4;
    --ink: #1b1b1b;
    --rule: #2a2a2a;
  }
  html, body {
    margin: 0;
    padding: 0;
    width: 1200px;
    height: 918px;
    overflow: hidden;
    background: var(--backdrop);
    font-family: "Roboto", Arial, sans-serif;
    color: var(--ink);
  }
  .sheet {
    width: 1200px;
    height: 918px;
    display: flex;
    align-items: center;
    justify-content: center;
    gap: 60px;
  }
  .card {
    position: relative;
    width: 520px;
    height: 318px;
    background: var(--card-stock);
    box-shadow: 0 2px 6px rgba(0,0,0,0.15);
    box-sizing: border-box;
  }
  .brand {
    text-align: center;
  }
  .brand-name {
    font-weight: 500;
    font-size: 40px;
    letter-spacing: 0.5px;
    line-height: 1;
  }
  .brand-tagline {
    font-weight: 500;
    font-size: 13px;
    letter-spacing: 2.5px;
    text-transform: uppercase;
    margin-top: 8px;
  }
  /* back of card */
  .card-back {
    display: flex;
    flex-direction: column;
    align-items: center;
    justify-content: center;
  }
  .card-back .web {
    margin-top: 46px;
    font-size: 13px;
    letter-spacing: 3.5px;
  }
  /* front of card */
  .card-front .brand {
    position: absolute;
    top: 56px;
    left: 0;
    right: 0;
  }
  .name-row {
    position: absolute;
    top: 164px;
    left: 24px;
    right: 24px;
    display: flex;
    align-items: center;
    gap: 10px;
  }
  .name-row .rule {
    flex: 1;
    height: 1px;
    background: var(--rule);
  }
  .person {
    font-weight: 500;
    font-size: 19px;
    text-transform: uppercase;
    white-space: nowrap;
  }
  .person .role {
    font-size: 14px;
  }
  .contact {
    position: absolute;
    left: 28px;
    bottom: 58px;
    font-size: 13.5px;
    line-height: 1.35;
  }
  .address {
    position: absolute;
    right: 28px;
    bottom: 34px;
    font-size: 13.5px;
    line-height: 1.35;
    text-align: right;
  }
</style>
</head>
<body>
<main class="sheet">
  <section class="card card-back" aria-label="Business card back">
    <div class="brand">
      <div class="brand-name">Basket Haven</div>
      <div class="brand-tagline">The Present Experts</div>
    </div>
    <div class="web">www.baskethaven.com.au</div>
  </section>

  <section class="card card-front" aria-label="Business card front">
    <div class="brand">
      <div class="brand-name">Basket Haven</div>
      <div class="brand-tagline">The Present Experts</div>
    </div>
    <div class="name-row">
      <span class="rule"></span>
      <span class="person">Alan Brooks <span class="role">- CEO/Founder</span></span>
      <span class="rule"></span>
    </div>
    <div class="contact">
      P : 1800 742 918<br>
      sales@baskethaven.com.au<br>
      www.baskethaven.com.au
    </div>
    <div class="address">
      Basket Haven Pty Ltd<br>
      518 Pelling Street<br>
      Carrow Vale, Victoria, 3071
    </div>
  </section>
</main>
</body>
</html>
```